Steel Company / Iron Railing Business Card Template

We are a custom steel fabrication company located in Trainer, PA. In business since 1979, we recently developed a new logo, and we're looking for a business card design to help display the new logo and our business. The name of the company is Kelbrook Forge Co.. The Office Phone number is (610) 555-0143. We fabricate and install custom "wrought iron" railings on our residential side, we also fabricate and erect structural steel (think cranes and steel beams in buildings) on our commercial side. Looking to get a business card template designed. Something modern, but professional. Clear and easy to read. Front should have all business and employee information including phone number(s), email address, business information, etc. back should spotlight logo.

Industry/Entity Type

Construction / Home Improvement

Contact Information for Business Card

Business information is Kelbrook Forge Co., 48 Dunmore Ave Suite 3305, Trainer, PA 19074. Phone number is (610) 555-0143. Website is www.kelbrookforge.example Business card should be for "Tom Pelling" with the job title "Sales & Estimating" but be editable for other employees. Tom's phone number is (610) 555-0178

Colors

Designer to choose colors to be used in the design.

Requirements
Must have
• Modern Feel, Design should be sized for standard business card sizing 3.5" x 2" (88.9mm x 50.8mm)

```html
<!DOCTYPE html>
<html lang="en">
<head>
<meta charset="UTF-8">
<title>Kelbrook Forge Co. — Business Card</title>
<link href="https://fonts.googleapis.com/css2?family=Montserrat:wght@400;500;700;800&display=swap" rel="stylesheet">
<style>
  :root {
    --page-bg: #e9e9ec;
    --card-bg: #ffffff;
    --brand-blue: #1f3a93;
    --brand-red: #d9413a;
    --text-gray: #3a3a3f;
  }
  * { box-sizing: border-box; margin: 0; padding: 0; }
  html, body {
    width: 1200px; height: 900px; overflow: hidden;
    background: var(--page-bg);
    font-family: "Montserrat", Arial, sans-serif;
  }
  .sheet {
    width: 1200px; height: 900px;
    display: flex; align-items: center; justify-content: center; gap: 40px;
  }
  .card {
    width: 540px; height: 309px;
    background: var(--card-bg);
    border-radius: 26px;
    box-shadow: 0 8px 24px rgba(0,0,0,0.12);
    position: relative;
    overflow: hidden;
  }
  .brand-mark {
    display: flex; align-items: center; gap: 12px;
  }
  .brand-mark__dot {
    width: 22px; height: 22px; border-radius: 50%;
    background: var(--brand-red); flex: none;
  }
  .brand-mark__name {
    color: var(--brand-blue);
    font-weight: 800;
    line-height: 1.05;
    text-transform: uppercase;
  }
  /* back: logo spotlight */
  .card--back { display: flex; align-items: center; justify-content: center; }
  .card--back .brand-mark__name { font-size: 40px; }
  .card--back .brand-mark__dot { width: 30px; height: 30px; }

  /* front: contact details */
  .card--front { display: flex; align-items: center; padding: 0 30px 0 34px; }
  .card--front .brand-mark { width: 200px; }
  .card--front .brand-mark__name { font-size: 24px; }
  .divider {
    width: 2px; height: 190px; background: var(--brand-blue);
    margin: 0 24px 0 20px; flex: none;
  }
  .contact { color: var(--text-gray); font-size: 13.5px; line-height: 1.55; }
  .contact__name {
    color: var(--brand-blue); font-weight: 800; font-size: 25px; line-height: 1.1;
  }
  .contact__title { font-size: 14px; margin-bottom: 8px; }
  .contact__row { display: flex; align-items: center; gap: 8px; }
  .contact__row svg { width: 12px; height: 12px; flex: none; fill: var(--brand-blue); }
</style>
</head>
<body>
<main class="sheet">
  <section class="card card--back" aria-label="Card back">
    <div class="brand-mark">
      <span class="brand-mark__dot"></span>
      <span class="brand-mark__name">Kelbrook<br>Forge Co.</span>
    </div>
  </section>

  <section class="card card--front" aria-label="Card front">
    <div class="brand-mark">
      <span class="brand-mark__dot"></span>
      <span class="brand-mark__name">Kelbrook<br>Forge Co.</span>
    </div>
    <div class="divider"></div>
    <div class="contact">
      <p class="contact__name">Tom Pelling</p>
      <p class="contact__title">Sales &amp; Estimating</p>
      <p>48 Dunmore Ave Suite 3305</p>
      <p>Trainer, PA 19074</p>
      <p class="contact__row">
        <svg viewBox="0 0 12 12" aria-hidden="true"><path d="M3 0h6a1 1 0 0 1 1 1v10a1 1 0 0 1-1 1H3a1 1 0 0 1-1-1V1a1 1 0 0 1 1-1zm0 1.5v8h6v-8z"/></svg>
        (610) 555-0178
      </p>
      <p class="contact__row">
        <svg viewBox="0 0 12 12" aria-hidden="true"><path d="M1 4c0-2 2-3 5-3s5 1 5 3v1H8.5V3.8h-5V5H1zM2.5 6h7l1.5 5H1z"/></svg>
        (610) 555-0143
      </p>
      <p class="contact__row">
        <svg viewBox="0 0 12 12" aria-hidden="true"><circle cx="6" cy="6" r="5.5"/></svg>
        www.kelbrookforge.example
      </p>
    </div>
  </section>
</main>
</body>
</html>
```